Texting While Driving/Distracted Driving Educational Poster

We are a design-driven nutrition, health, and wellness educational company looking for a fresh, eye-catching educational poster design to promote attentive driving, primarily to young and new drivers. Young, inexperienced drivers (under 20) have the highest proportion of distraction-related fatal crashes, with talking and texting being the most commonly recognized distraction. We hope to draw attention to this issue with an engaging, persuasive poster. The poster will be printed and available for purchase on our website and print catalogs.

Target Market(s)

The audience is American teen to adult drivers and the buyer is educators and healthcare professionals.

Requirements
Must have
• The poster must be 18" x 24" trim size, all fonts in outlines, full color art converted to CMYK.

```html
<!DOCTYPE html>
<html lang="en">
<head>
<meta charset="UTF-8">
<title>Don't Text and Drive — Public Service Announcement</title>
<link rel="stylesheet" href="https://fonts.googleapis.com/css2?family=Arimo:wght@400;700&display=swap">
<style>
  :root {
    --ink-night: #08090b;
    --paper-white: #ffffff;
    --signal-blue: #2f5eff;
    --rule-grey: #9a9ca0;
  }
  * { margin: 0; padding: 0; box-sizing: border-box; }
  html, body {
    width: 900px;
    height: 1200px;
    overflow: hidden;
    background: var(--ink-night);
  }
  .poster {
    position: relative;
    width: 900px;
    height: 1200px;
    background: var(--ink-night);
    font-family: "Arimo", Arial, sans-serif;
    color: var(--paper-white);
  }
  .headline {
    position: absolute;
    left: 74px;
    top: 30px;
    font-weight: 700;
    font-size: 139px;
    line-height: 167px;
    letter-spacing: -0.5px;
  }
  .headline span { display: block; }
  .headline .accent { color: var(--signal-blue); margin-left: -3px; }
  .tagline {
    position: absolute;
    left: 75px;
    top: 990px;
    font-weight: 700;
    font-size: 33px;
    line-height: 30px;
    white-space: nowrap;
  }
  .tagline .label { color: var(--signal-blue); display: block; }
  .tagline .sponsor { display: block; }
  .divider {
    position: absolute;
    left: 74px;
    top: 1103px;
    width: 704px;
    height: 1px;
    background: var(--rule-grey);
  }
  .brand-name {
    position: absolute;
    right: 122px;
    top: 1125px;
    font-size: 13px;
    font-weight: 400;
    color: var(--paper-white);
  }
</style>
</head>
<body>
  <main class="poster">
    <h1 class="headline">
      <span>DONT</span>
      <span>TEXT</span>
      <span class="accent">AND</span>
      <span>DRIVE</span>
    </h1>
    <p class="tagline">
      <span class="label">Public Service Announcement</span>
      <span class="sponsor">brought to you by drivers who text and drive</span>
    </p>
    <div class="divider"></div>
    <div class="brand-name">Steadyway</div>
  </main>
</body>
</html>
```